MORU-TEK vegan protein

Hi
We need a vegan protein label and logo for our company
MORU-TEK
We made a quick sketch in the type of way we want it But you can always make it better
Dont mind the logo we sketched please come up with something else
Left side of the label please the color of the taste So brown red vanille we need 3 designs for Chocolate, strawberry and vanilla
Backside: leave nutrition faces blank,
One square text with: Pea Protein derived and extracted from organic grean split peas. It is a great source of fiber (helps with digestion and less bloating), vitamines and minerals. Studies have shown that the intake of pea protein can reduce high blood pressure and that it can be used for prevention and controll of diabetes as it has minimal effect on blood glucose levels and insulin response.
One square with suggested use:
Add 1 or 2 scoops to a blender, shaker or glass with cold water or your favorite beverage (various amount of liquid to achieve your desired taste). Shake or mix well before consumption.
Distributed by:
DRAVEN COMPANY BV
THE NETHERLANDS
Please make it look amazing elegant and premium elite looking
It will be made on a alu bag like a send In the pictures

```html
<!DOCTYPE html>
<html lang="en">
<head>
<meta charset="utf-8">
<title>MORU-TEK Organic Vegan Protein – Vanilla Label</title>
<link href="https://fonts.googleapis.com/css2?family=Montserrat:wght@500;700;800;900&family=Roboto+Condensed:wght@400&display=swap" rel="stylesheet">
<style>
  :root {
    --bg: #4e4e51;
    --label: #ffffff;
    --flavour: #f3eaaa;
    --flavour-line: #efe3a0;
    --ink: #333335;
    --dot-dark: #6d6e71;
    --dot-light: #a7a9ac;
    --vanilla-a: #f6e27a;
    --vanilla-b: #6b4a2e;
  }
  * { margin: 0; padding: 0; box-sizing: border-box; }
  html, body { width: 1200px; height: 922px; overflow: hidden; background: var(--bg); }
  body { position: relative; font-family: "Montserrat", sans-serif; color: var(--ink); }

  .label {
    position: absolute;
    left: 340px; top: 41px;
    width: 495px; height: 800px;
    background: var(--label);
    transform: scale(1.05);
    transform-origin: top left;
    overflow: hidden;
  }
  .flavour-band {
    position: absolute; left: 0; top: 0;
    width: 134px; height: 100%;
    background: var(--flavour);
  }
  .brand-vertical {
    position: absolute; left: 88px; top: 427px;
    transform: translate(-50%, -50%) rotate(-90deg);
    font-weight: 900; font-size: 74px; letter-spacing: 0;
    white-space: nowrap; line-height: 1;
  }
  .flavour-badge {
    position: absolute; left: 18px; top: 670px;
    width: 100px; height: 100px; border-radius: 50%;
    background: var(--label);
    border: 2px solid var(--flavour-line);
    display: flex; align-items: center; justify-content: center;
  }
  .flavour-art {
    width: 76px; height: 40px; border-radius: 20px;
    background: radial-gradient(circle at 50% 40%, var(--vanilla-a) 0 30%, var(--vanilla-b) 75%);
    opacity: .85;
  }

  .content { position: absolute; left: 134px; top: 0; right: 0; height: 100%; text-align: center; }
  .content > * { white-space: nowrap; }
  .title-main { position: absolute; left: 0; right: 0; top: 146px; font-weight: 800; font-size: 56px; line-height: 1; }
  .title-sub { position: absolute; left: 0; right: 0; top: 205px; font-weight: 800; font-size: 32px; line-height: 1; }

  .brand-mark {
    position: absolute; left: 34px; top: 270px;
    width: 282px; height: 150px;
    display: flex; align-items: center; justify-content: center;
    font-weight: 900; font-size: 42px; color: var(--flavour-line); letter-spacing: 1px;
  }

  .claim-big { position: absolute; left: 0; right: 0; top: 454px; font-weight: 900; font-size: 100px; line-height: 1; }
  .claim-sub { position: absolute; left: 0; right: 0; top: 551px; font-weight: 800; font-size: 36px; line-height: 1; }

  .facts { position: absolute; left: 0; top: 0; width: 100%; height: 100%; }
  .fact {
    position: absolute; width: 66px; height: 66px; border-radius: 50%;
    display: flex; flex-direction: column; align-items: center; justify-content: center;
    color: #fff; font-family: "Roboto Condensed", sans-serif; line-height: 1.05;
    font-size: 9px; text-transform: uppercase;
  }
  .fact strong { font-weight: 400; font-size: 15px; text-transform: none; }
  .fact.dark { background: var(--dot-dark); }
  .fact.light { background: var(--dot-light); }

  .net-weight {
    position: absolute; left: 86px; top: 735px;
    width: 177px; height: 37px;
    background: var(--flavour);
    border-radius: 18px 6px 18px 6px;
    display: flex; align-items: center; justify-content: center;
    font-weight: 700; font-size: 15px;
  }
</style>
</head>
<body>
  <main class="label">
    <div class="flavour-band"></div>
    <div class="brand-vertical">MORU-TEK</div>
    <div class="flavour-badge">
      <div class="flavour-art" role="img" aria-label="Vanilla flower with vanilla pods"></div>
    </div>

    <section class="content">
      <h1 class="title-main">ORGANIC</h1>
      <h2 class="title-sub">VEGAN PROTEIN</h2>

      <div class="brand-mark">MORU-TEK</div>

      <p class="claim-big">100%</p>
      <p class="claim-sub">PLANT BASED</p>

      <div class="facts">
        <div class="fact dark"  style="left:16px;top:622px"><strong>0</strong>Sugare</div>
        <div class="fact light" style="left:77px;top:632px"><strong>7g</strong>Organic</div>
        <div class="fact dark"  style="left:143px;top:622px"><strong>21 g</strong>Protein</div>
        <div class="fact light" style="left:205px;top:632px"><strong>GF</strong></div>
        <div class="fact dark"  style="left:270px;top:617px">Super<br>Food<br>Vitamines</div>
      </div>

      <div class="net-weight">Net Wt. 700 g</div>
    </section>
  </main>
</body>
</html>
```